Transform Your Giving

I need a tri-fold brochure that will fit in a standard number 10 business envelope. Harborline and Steadfast Services is a charitable nonprofit. The goal of this brochure is to stimulate people into thinking about other ways to make a donation. The design should communicate the essential information on donation options, create a sense of professional integrity, be graphically sharp, easy to read and laid out in a way that doesn't make the material appear crowded.

```html
<!DOCTYPE html>
<html lang="en">
<head>
<meta charset="utf-8">
<title>Transform Your Giving – Tri-fold Brochure</title>
<link rel="stylesheet" href="https://fonts.googleapis.com/css2?family=Poppins:ital,wght@0,400;0,500;0,600;0,700;0,800;1,400;1,600&display=swap">
<style>
:root{
  --navy:#2b2a7e;
  --navy-dark:#23226b;
  --green:#3fb549;
  --green-light:#d8f5d6;
  --cream:#fbf9f0;
  --ink:#3a3a48;
  --stage:#d6d6d8;
  --white:#ffffff;
}
*{box-sizing:border-box;margin:0;padding:0}
html,body{width:1200px;height:2162px;overflow:hidden}
body{background:var(--stage);font-family:"Poppins",sans-serif;color:var(--ink);position:relative}
.spread{position:absolute;left:30px;width:1140px;height:482px;display:flex;box-shadow:0 6px 18px rgba(0,0,0,.18)}
.spread--outside{top:580px}
.spread--inside{top:1102px}
.panel{position:relative;width:380px;height:482px;overflow:hidden}
.panel--white{background:var(--white)}
.panel--navy{background:var(--navy);color:var(--white)}
.panel--cover{background:linear-gradient(135deg,var(--cream) 40%,#e3f7df 100%)}
.abs{position:absolute}
.photo{position:absolute}
.wordmark{position:absolute;left:0;right:0;text-align:center;font-weight:700;font-size:17px;letter-spacing:.5px;color:var(--navy)}
.wordmark--light{color:var(--white)}
.wordmark .dot{display:inline-block;width:10px;height:10px;border-radius:50%;background:var(--green);margin-right:6px;vertical-align:1px}
.h-sec{font-weight:700;font-size:11.5px;color:var(--navy);line-height:1.15;text-transform:uppercase}
.h-sec em{font-style:normal;color:var(--green)}
.body{font-size:7.6px;line-height:1.32}
.lede{font-size:7.8px;font-style:italic;font-weight:600;line-height:1.3;color:var(--navy)}
.icon-ring{width:30px;height:30px;border-radius:50%;border:1.5px solid var(--navy);display:flex;align-items:center;justify-content:center;background:var(--white)}
.icon-ring svg{width:16px;height:16px}
/* impact box */
.impact{left:36px;top:36px;width:308px;height:160px;border:1px solid var(--green);border-top:none;border-radius:0 0 8px 8px;padding:0 10px}
.impact__title{position:absolute;top:-8px;left:-1px;background:var(--white);padding-right:8px;font-size:12px;font-weight:700;color:var(--navy)}
.impact__title em{font-style:normal;color:var(--green)}
.impact .body{margin-top:14px}
.opts{display:grid;grid-template-columns:1fr 1fr;row-gap:6px;margin-top:8px;font-size:8px;font-weight:500;color:var(--navy)}
.opt{display:flex;align-items:center;gap:6px}
.opt i{width:15px;height:15px;border-radius:50%;border:1.2px solid var(--navy);display:inline-block;background:radial-gradient(circle,var(--green) 0 2.5px,transparent 3px)}
/* navy reach panel */
.reach{left:30px;right:30px;top:84px;text-align:center;font-size:9.4px;font-weight:700;line-height:1.25}
.reach .g{color:var(--green)}
.quote-mark{left:0;right:0;top:138px;text-align:center;font-size:42px;font-weight:800;color:var(--green);line-height:1}
.quote{left:52px;width:276px;top:162px;border:1px solid var(--green);border-radius:10px;overflow:hidden}
.quote p{font-style:italic;font-size:11px;text-align:center;padding:8px 10px 6px;line-height:1.3}
.quote b{display:block;background:var(--green);text-align:center;font-size:11px;font-weight:700;padding:4px 0;letter-spacing:.3px}
.will{left:0;right:0;text-align:center;font-size:9.5px}
.will-url{left:90px;width:200px;top:258px;border:1.5px solid var(--green);border-radius:12px;text-align:center;font-size:14px;font-weight:700;color:var(--green);letter-spacing:.8px;line-height:19px}
.contact{left:36px;width:306px;top:302px;height:180px;background:var(--green);border-radius:12px 12px 0 0;text-align:center}
.contact__tab{position:absolute;left:90px;width:126px;top:-2px;background:var(--white);color:var(--navy);font-weight:700;font-size:11.5px;line-height:24px;border-radius:0 0 12px 12px}
.contact h3{margin-top:34px;font-size:12.5px;font-weight:700;color:var(--navy)}
.contact p.sub{font-size:9px;color:var(--navy);line-height:1.2}
.contact-lines{display:grid;grid-template-columns:auto auto;justify-content:center;column-gap:10px;row-gap:4px;margin-top:10px;font-size:6.4px;color:var(--navy);text-align:left}
.contact-lines span{display:flex;align-items:center;gap:4px}
.contact-lines svg{width:9px;height:9px;flex:none}
.follow{margin-top:10px;font-size:8px;color:var(--navy)}
.disclaim{margin:6px 14px 0;font-size:4.4px;color:var(--navy);line-height:1.35}
/* cover */
.cover-title{left:0;right:0;top:300px;text-align:center;font-weight:800;line-height:1}
.cover-title .t1{display:block;font-size:31px;color:var(--navy)}
.cover-title .t2{display:block;font-size:37px;color:var(--green)}
.cover-rule{left:40px;right:40px;top:380px;height:1px;background:#9aa}
.cover-rule::after{content:"";position:absolute;left:50%;margin-left:-16px;top:-1.5px;width:32px;height:4px;border-radius:2px;background:var(--navy)}
.tags{left:0;right:0;top:390px;text-align:center;font-size:10px;font-weight:600;color:var(--navy)}
.tags span{display:inline-flex;align-items:center;gap:3px;margin:0 5px}
.tags i{width:8px;height:8px;border-radius:50%;background:var(--navy);display:inline-block}
.discover{left:40px;right:40px;top:410px;text-align:center;font-size:10.5px;line-height:1.3;color:var(--navy-dark)}
.site{left:0;right:0;text-align:center;font-size:11px;font-weight:500;letter-spacing:1.2px;color:var(--navy)}
.site b{color:var(--green);font-weight:600}
.site--light{color:var(--white)}
/* inside */
.sec-head{display:flex;gap:8px;align-items:flex-start}
.how{font-weight:700;font-size:11px;color:var(--navy)}
.how em{font-style:normal;color:var(--green)}
.panel--navy .how{color:var(--white)}
.panel--navy .h-sec{color:var(--white)}
.panel--navy .lede{color:var(--white)}
.ticks{list-style:none;font-size:6.6px;line-height:1.3}
.ticks li{position:relative;padding-left:12px;margin-bottom:4px}
.ticks li::before{content:"";position:absolute;left:0;top:1px;width:7px;height:7px;border-radius:50%;background:var(--green)}
.small{font-size:6.6px;line-height:1.32}
</style>
</head>
<body>

<!-- OUTSIDE SPREAD -->
<section class="spread spread--outside">
  <article class="panel panel--white">
    <div class="abs impact">
      <h2 class="impact__title">THE IMPACT <em>OF YOUR GIFT</em></h2>
      <p class="body">Your generosity drives our mission. With every Smart gift you’re supporting Harborline and Steadfast Services. Join our community of Smart Givers today and make an enduring impact. With Smart Giving your generosity reaches further. Begin your Smart Giving journey with us today.</p>
      <div class="opts">
        <span class="opt"><i></i>Crypto</span><span class="opt"><i></i>QCDs</span>
        <span class="opt"><i></i>DAF’s</span><span class="opt"><i></i>Charitable Annuity</span>
        <span class="opt"><i></i>Stocks &amp; Securities</span>
      </div>
    </div>
    <div class="photo" role="img" aria-label="Photo of a smiling nurse hugging an elderly man in a wheelchair in a garden" style="left:0;top:205px;width:380px;height:277px;background:linear-gradient(180deg,#ededed 0%,#a9a9a9 45%,#8f95a8 100%)"></div>
  </article>

  <article class="panel panel--navy">
    <div class="wordmark wordmark--light" style="top:34px"><span class="dot"></span>Harborline &amp; Steadfast</div>
    <p class="abs reach"><span class="g">To learn more about Smart Giving Options and how they can benefit you and</span> Harborline and Steadfast Services, please reach out to our team. We’re here to help you navigate these giving methods and answer any question you may have.</p>
    <div class="abs quote-mark">“</div>
    <div class="abs quote"><p>Being kind to others is a way of being good to yourself.</p><b>MIRIAM OSTRANDER</b></div>
    <p class="abs will" style="top:240px">If you do not have a will, go to</p>
    <div class="abs will-url">www.EasyLegacy.org</div>
    <p class="abs will" style="top:282px">In 20 minutes you can have a legal will – for free</p>
    <div class="abs contact">
      <div class="contact__tab">CONTACT US</div>
      <h3>HAVE MORE QUESTION?</h3>
      <p class="sub">Please contact us at Harborline and<br>Steadfast</p>
      <div class="contact-lines">
        <span><svg viewBox="0 0 10 10"><circle cx="5" cy="5" r="5" fill="#2b2a7e"/><path d="M3.2 2.6l1 1-.5.7c.4.8.9 1.3 1.6 1.6l.7-.5 1 1-.6.8C4.8 7 3 5.2 2.8 3.2z" fill="#fff"/></svg>555-014-2200 (ext. 100)</span>
        <span><svg viewBox="0 0 10 10"><circle cx="5" cy="5" r="5" fill="#2b2a7e"/><path d="M5 2.2a1.8 1.8 0 0 1 1.8 1.8C6.8 5.4 5 7.8 5 7.8S3.2 5.4 3.2 4A1.8 1.8 0 0 1 5 2.2z" fill="#fff"/></svg>1420 Alder Row, Suite 4 Fairhaven, ND 58000</span>
        <span><svg viewBox="0 0 10 10"><circle cx="5" cy="5" r="5" fill="#2b2a7e"/><rect x="2.5" y="3.3" width="5" height="3.4" fill="#fff"/><path d="M2.5 3.3L5 5.2 7.5 3.3" stroke="#2b2a7e" stroke-width=".6" fill="none"/></svg>mreyes@harborlinesvc.org</span>
        <span><svg viewBox="0 0 10 10"><circle cx="5" cy="5" r="5" fill="#2b2a7e"/><circle cx="5" cy="5" r="2.6" fill="none" stroke="#fff" stroke-width=".6"/><path d="M2.4 5h5.2M5 2.4v5.2" stroke="#fff" stroke-width=".5"/></svg>www.harborlinesvc.org</span>
      </div>
      <p class="follow">Follow us</p>
      <p class="disclaim">This material has been prepared for informational purposes only and is not intended to provide tax, accounting, or legal advice. Harborline and Steadfast Services is not a fiduciary. Please consult your tax advisor before making a decision about Smart Giving.</p>
    </div>
  </article>

  <article class="panel panel--cover">
    <div class="wordmark" style="top:40px"><span class="dot"></span>Harborline &amp; Steadfast</div>
    <svg class="abs" style="left:0;top:90px" width="380" height="210" viewBox="0 0 380 210">
      <path d="M0 190 L110 110 L150 190 Z" fill="#2b2a7e"/>
      <path d="M380 190 L270 110 L230 190 Z" fill="#2b2a7e"/>
      <path d="M72 160 A118 118 0 1 1 308 160" fill="none" stroke="#3fb549" stroke-width="1.5" stroke-dasharray="5 4"/>
      <path d="M0 200 Q190 150 380 200 L380 210 Q190 162 0 210 Z" fill="#3fb549"/>
      <g fill="#fff" stroke="#2b2a7e" stroke-width="1.3">
        <circle cx="85" cy="100" r="11"/><circle cx="60" cy="148" r="10"/><circle cx="118" cy="58" r="10"/>
        <circle cx="262" cy="58" r="10"/><circle cx="295" cy="100" r="10"/><circle cx="318" cy="148" r="10"/>
      </g>
      <g fill="#3fb549"><circle cx="85" cy="100" r="3"/><circle cx="60" cy="148" r="3"/><circle cx="118" cy="58" r="3"/><circle cx="262" cy="58" r="3"/><circle cx="295" cy="100" r="3"/><circle cx="318" cy="148" r="3"/></g>
    </svg>
    <div class="photo" role="img" aria-label="Circular photo of a caregiver helping a smiling elderly woman in a wheelchair" style="left:92px;top:95px;width:196px;height:196px;border-radius:50%;background:radial-gradient(circle at 50% 40%,#dfe7f1,#8aa6c8 70%,#6d84b0)"></div>
    <h1 class="abs cover-title"><span class="t1">TRANSFORM</span><span class="t2">YOUR GIVING</span></h1>
    <div class="abs cover-rule"></div>
    <p class="abs tags"><span><i></i>Be Strategic</span>|<span><i></i>Be Smart</span></p>
    <p class="abs discover">Discover the impact of Smart Giving with Harborline and Steadfast Services</p>
    <p class="abs site" style="top:448px">www.<b>harborlinesvc</b>.org</p>
  </article>
</section>

<!-- INSIDE SPREAD -->
<section class="spread spread--inside">
  <article class="panel panel--white">
    <p class="abs body" style="left:36px;right:36px;top:30px">We would like to introduce you to five Strategic and Smart ways to give that could potentially be more beneficial to you compared to traditional cash donations. We encourage you to keep this information as a guide for your future contributions.</p>
    <div class="abs sec-head" style="left:36px;right:36px;top:82px">
      <div class="icon-ring"><svg viewBox="0 0 16 16"><path d="M3 13V9M6 13V7M9 13V8M12 13V5" stroke="#2b2a7e" stroke-width="1.6"/></svg></div>
      <div><h3 class="h-sec">Gifts of stocks or appreciated <em>assets strategic &amp; smart</em></h3><p class="lede" style="margin-top:3px">Consider your long-term publicly traded stock as a way to give to your favorite charity.</p></div>
    </div>
    <p class="abs body" style="left:36px;right:36px;top:140px">You can make a significantly bigger impact when you donate long-term appreciated securities, including stock, mutual funds, and bonds, directly to your favorite charity.</p>
    <h4 class="abs how" style="left:36px;top:180px">HOW DOES <em>IT WORK?</em></h4>
    <p class="abs body" style="left:36px;right:36px;top:198px;text-align:justify">When you donate stock to a charity, you will generally take a tax deduction for the full market value. Because you are donating stock, your contribution and tax deduction may be significantly higher than contributing the after-tax proceeds. The same benefits apply when you donate mutual funds or bonds.</p>
    <div class="photo" role="img" aria-label="Photo of a caregiver walking arm in arm with an elderly woman in a sunny park" style="left:0;top:262px;width:380px;height:220px;background:linear-gradient(180deg,rgba(255,255,255,1) 0%,#cfdcc8 30%,#8fae7d 75%,#6f8f62 100%)"></div>
  </article>

  <article class="panel panel--navy">
    <div class="abs sec-head" style="left:38px;right:30px;top:28px">
      <div class="icon-ring" style="border-color:var(--green)"><svg viewBox="0 0 16 16"><path d="M3 13h10M4 12V7M7 12V7M9 12V7M12 12V7M2.5 6L8 3l5.5 3z" stroke="#2b2a7e" stroke-width="1.2" fill="none"/></svg></div>
      <div><h3 class="h-sec">Donor-Advised Fund (DAF)<br><em>Strategic &amp; Smart</em></h3><p class="lede" style="margin-top:4px">Consider a DAF – a simple, flexible, and tax-advantageous way to give to your favorite charities.</p></div>
    </div>
    <p class="abs body" style="left:38px;right:30px;top:96px">A Donor-Advised Fund (DAF), is like a charitable investment account for the sole purpose of supporting your favorite charities.</p>
    <h4 class="abs how" style="left:38px;top:124px;font-size:12px">HOW DOES <em>IT WORK?</em></h4>
    <p class="abs body" style="left:38px;right:30px;top:142px;text-align:justify">You establish a DAF and contribute cash, stocks, or non-publicly traded assets, cryptocurrency, and private company stock to be eligible for an immediate tax deduction. Those funds are contributed for tax-free growth. You can recommend grants be made from your DAF to any IRS qualified public charity.</p>
    <p class="abs site site--light" style="left:38px;right:auto;top:222px">www.<b>harborlinesvc</b>.org</p>
    <svg class="abs" style="left:0;top:320px" width="380" height="162" viewBox="0 0 380 162"><path d="M-20 162 L190 20 L400 162 Z" fill="#3fb549"/></svg>
    <div class="photo" role="img" aria-label="Photo of a doctor handing a glass of water to an elderly man in a wheelchair" style="left:60px;top:252px;width:280px;height:230px;border-radius:40% 40% 0 0;background:linear-gradient(160deg,#3d3c8c 0%,#6c7fb0 45%,#e6e8ef 100%)"></div>
  </article>

  <article class="panel panel--white">
    <div class="abs sec-head" style="left:22px;right:22px;top:24px">
      <div class="icon-ring"><svg viewBox="0 0 16 16"><rect x="3" y="7" width="10" height="6" fill="none" stroke="#2b2a7e" stroke-width="1.2"/><rect x="2.5" y="5" width="11" height="2.2" fill="none" stroke="#2b2a7e" stroke-width="1.2"/><path d="M8 5v8" stroke="#2b2a7e" stroke-width="1.2"/></svg></div>
      <div><h3 class="h-sec">Qualified Charitable Distributions <em>(QCDs) Strategic &amp; Smart</em></h3><p class="lede" style="margin-top:2px">Consider a QCD – when planning your IRA withdrawal strategy…and donate to your favorite charity.</p></div>
    </div>
    <p class="abs small" style="left:22px;right:22px;top:72px">IRA owners at age 70 ½ or over can transfer dollars from their IRA to charity tax-free each year. These transfers known as Qualified Charitable Distributions (QCDs) offer eligible older Americans a great way to easily give to charity.</p>
    <h4 class="abs how" style="left:22px;top:104px">HOW DOES <em>IT WORK?</em></h4>
    <p class="abs small" style="left:22px;right:22px;top:120px">Are you 72 and required to take a minimum distribution (RMD) from your IRA but do not need the funds? Consider a Qualified Charitable Distribution. Normally, distributions from a traditional IRA are taxable when received. With a QCD, these distributions become tax-free when paid directly from the IRA to your favorite eligible charity. An IRA owner wishing to make a QCD should contact their IRA trustee, allowing time to complete the transaction before the end of the year.</p>

    <div class="abs" style="left:22px;width:160px;top:186px">
      <div class="sec-head"><div class="icon-ring"><svg viewBox="0 0 16 16"><circle cx="8" cy="8" r="5" fill="none" stroke="#2b2a7e" stroke-width="1.3"/><path d="M10 6.3a2.4 2.4 0 1 0 0 3.4" fill="none" stroke="#2b2a7e" stroke-width="1.3"/></svg></div><h3 class="h-sec" style="font-size:9.5px">Cryptocurrency<br><em>Strategic &amp; Smart</em></h3></div>
      <p class="lede" style="font-size:6.8px;margin-top:4px">Consider donating Bitcoin and other cryptocurrencies to your favorite charity.</p>
      <p class="small" style="margin-top:3px">Bitcoin and other cryptocurrencies can be donated to charity just like other appreciated assets such as stocks. Before you sell bitcoin, consider donating your bitcoin directly to a favorite charity.</p>
      <h4 class="how" style="margin-top:5px;font-size:10px">HOW DOES <em>IT WORK?</em></h4>
      <p class="small">Many donors find it useful to open a Donor-Advised Fund (DAF). This strategy includes two significant benefits.</p>
      <ul class="ticks" style="margin-top:4px">
        <li>Your tax deduction will be equal to the fair market value of the donated bitcoin.</li>
        <li>Your donation may eliminate capital gains taxes AND your charity will receive 100% of the value.</li>
      </ul>
      <p class="small">Often charities are not able to accept direct donations of crypto, so using a DAF is a great way to donate.</p>
    </div>

    <div class="abs" style="left:196px;width:162px;top:186px">
      <div class="sec-head"><div class="icon-ring"><svg viewBox="0 0 16 16"><path d="M8 12.5s-4.5-2.8-4.5-5.6A2.2 2.2 0 0 1 8 5.6a2.2 2.2 0 0 1 4.5 1.3C12.5 9.7 8 12.5 8 12.5z" fill="none" stroke="#2b2a7e" stroke-width="1.3"/></svg></div><h3 class="h-sec" style="font-size:9.5px">Charitable Gift Annuity<br><em>Strategic &amp; Smart</em></h3></div>
      <p class="lede" style="font-size:6.8px;margin-top:4px">Consider establishing a Charitable Gift Annuity</p>
      <p class="small" style="margin-top:3px">You make a donation to a single charity. The gift is set aside in a reserve account and invested.</p>
      <h4 class="how" style="margin-top:6px;font-size:10px">HOW DOES <em>IT WORK?</em></h4>
      <p class="small" style="text-align:justify">A charitable gift annuity is a contract between a donor and a charity. As a donor, you make a sizable gift to charity using cash, securities, or possibly other assets. This money is then invested. In return, you become eligible to take a partial tax deduction for your donation, plus you receive a fixed stream of income from the charity for the rest of your life. At the end of your life (as well as your spouse’s, if you’re giving as a couple), the charity receives the remainder of the gift.</p>
      <div class="wordmark" style="position:relative;margin-top:14px;font-size:11px"><span class="dot" style="width:7px;height:7px"></span>Harborline &amp; Steadfast</div>
      <p class="site" style="position:relative;margin-top:6px;font-size:10px">www.<b>harborlinesvc</b>.org</p>
    </div>
  </article>
</section>

</body>
</html>
```